Brochure Design For Beauty Salon

We have an existing brochure for our beauty salon business which has been designed in-house.

We need a designer to refresh the look and feel of the brochure, which is intended for print. The print format will be 210mmx210mm (square, stapled).

We need a design for each and every page of the brochure, including the front and back covers.

We are looking for a fresh modern design, quite close to what we already have, but looking more slick and professional.

The primary colors are white, grey and purple. The final design will communicate luxury, prestige and cleanliness and have a heavy focus on creating the feeling of space within each page.

Target Market(s)

Professional Women, aged 20-45

Industry/Entity Type

Beauty Salon

Font styles to use
Sans Serif
Other font styles liked:
• Helvetica

Requirements
Must have
• The project must be ready for print on square paper 210x210mm

```html
<!DOCTYPE html>
<html lang="en">
<head>
<meta charset="utf-8">
<title>Amara Lane – Treatment Menu Covers</title>
<link rel="stylesheet" href="https://fonts.googleapis.com/css2?family=Questrial&family=Raleway:wght@700&family=Yellowtail&family=Montserrat:wght@600&display=swap">
<style>
  :root {
    --stage: #4a403c;
    --paper: #f3f1f2;
    --paper-tint: #ece4ea;
    --plum: #a3336b;
    --ink: #4f4d50;
    --ink-soft: #5e5c60;
    --label: #ffffff;
    --skin-light: #f3ddd2;
    --skin-mid: #e6c2b2;
    --hair: #3b3230;
  }
  html, body {
    margin: 0; padding: 0;
    width: 1200px; height: 1200px;
    overflow: hidden;
    background: var(--stage);
  }
  .canvas { position: relative; width: 1200px; height: 1200px; }
  .side-label {
    position: absolute; top: 276px; width: 544px;
    text-align: center; color: var(--label);
    font: 30px "Questrial", sans-serif; letter-spacing: 0.5px;
  }
  .cover {
    position: absolute; top: 328px; width: 544px; height: 544px;
    overflow: hidden;
    background:
      radial-gradient(circle at 20% 10%, var(--paper-tint), transparent 45%),
      radial-gradient(circle at 80% 85%, var(--paper-tint), transparent 40%),
      var(--paper);
  }
  .cover--front { left: 36px; }
  .cover--back { left: 620px; }
  .footer-band {
    position: absolute; left: 0; bottom: 0; width: 100%; height: 33px;
    background: var(--plum);
  }
  .footer-url {
    position: absolute; left: 0; bottom: 7px; width: 100%;
    text-align: center; color: #fff;
    font: 14px "Questrial", sans-serif; letter-spacing: 4.5px;
  }
  .portrait { position: absolute; }
  .portrait--front {
    left: 0; top: 36px; width: 400px; height: 475px;
    background: radial-gradient(ellipse 42% 48% at 47% 45%, var(--skin-light), var(--skin-mid) 70%, transparent 100%);
  }
  .portrait--back {
    left: 136px; top: 16px; width: 408px; height: 528px;
    background: linear-gradient(90deg, transparent 0%, var(--skin-light) 35%, var(--skin-mid) 100%);
  }
  .brand-block { position: absolute; text-align: center; }
  .brand-block--front { left: 250px; width: 290px; top: 86px; }
  .brand-block--back { left: 30px; width: 230px; top: 212px; }
  .brand-name {
    margin: 0; color: var(--ink-soft);
    font: 400 37px "Questrial", sans-serif; letter-spacing: 2px;
  }
  .brand-block--back .brand-name { font-size: 30px; }
  .brand-sub {
    margin: 6px 0 0; color: var(--ink-soft);
    font: 19px "Questrial", sans-serif; letter-spacing: -0.5px;
  }
  .brand-block--back .brand-sub { font-size: 16px; margin-top: 4px; }
  .welcome { position: absolute; left: 250px; width: 296px; top: 228px; text-align: center; }
  .welcome-script {
    margin: 0; color: var(--plum);
    font: 44px "Yellowtail", cursive; line-height: 1;
  }
  .welcome-name {
    margin: 6px 0 0; color: var(--ink);
    font: 700 33px "Raleway", sans-serif; letter-spacing: 1px;
  }
  .welcome-tag {
    display: flex; align-items: center; gap: 6px; margin-top: 2px;
    color: var(--plum); font: 600 13px "Montserrat", sans-serif; letter-spacing: 5px;
  }
  .welcome-tag::before, .welcome-tag::after {
    content: ""; flex: 1; height: 1px; background: #8a878b;
  }
  .contact-list { position: absolute; left: 60px; top: 304px; list-style: none; margin: 0; padding: 0; }
  .contact-item {
    display: flex; align-items: flex-start; gap: 8px; margin-bottom: 8px;
    color: var(--ink); font: 12px "Questrial", sans-serif; line-height: 1.2;
  }
  .contact-item--phone { font-size: 16px; }
  .contact-item svg { flex: none; width: 18px; height: 18px; }
</style>
</head>
<body>
<main class="canvas">
  <div class="side-label" style="left:36px">FRONT</div>
  <div class="side-label" style="left:620px">BACK</div>

  <section class="cover cover--front">
    <div class="portrait portrait--front" role="img" aria-label="Portrait photograph of a woman with hair pulled back, hands framing her face"></div>
    <div class="brand-block brand-block--front">
      <h1 class="brand-name">Amara Lane</h1>
      <p class="brand-sub">Treatment Menu</p>
    </div>
    <div class="welcome">
      <p class="welcome-script">welcome to</p>
      <p class="welcome-name">THE AMARA LANE</p>
      <div class="welcome-tag">BEAUTY SALON</div>
    </div>
    <div class="footer-band"></div>
    <div class="footer-url">www.amaralane.co.uk</div>
  </section>

  <section class="cover cover--back">
    <div class="footer-band"></div>
    <div class="portrait portrait--back" role="img" aria-label="Portrait photograph of a woman touching her chin, bare shoulders"></div>
    <div class="brand-block brand-block--back">
      <h2 class="brand-name">Amara Lane</h2>
      <p class="brand-sub">Treatment Menu</p>
    </div>
    <ul class="contact-list">
      <li class="contact-item contact-item--phone">
        <svg viewBox="0 0 20 20" aria-hidden="true"><rect x="3" y="2" width="14" height="16" rx="3" fill="none" stroke="var(--plum)" stroke-width="2"/><rect x="8" y="6" width="6" height="8" fill="var(--plum)"/></svg>
        020 7946 0321
      </li>
      <li class="contact-item">
        <svg viewBox="0 0 20 20" aria-hidden="true"><path d="M10 2 L19 10 H16 V18 H12 V13 H8 V18 H4 V10 H1 Z" fill="var(--plum)"/></svg>
        <span>48 Orchard Row<br>Elmhurst Green, N9 4QT</span>
      </li>
      <li class="contact-item">
        <svg viewBox="0 0 20 20" aria-hidden="true"><circle cx="10" cy="10" r="8" fill="none" stroke="var(--plum)" stroke-width="1.6"/><ellipse cx="10" cy="10" rx="3.5" ry="8" fill="none" stroke="var(--plum)" stroke-width="1.4"/><line x1="2" y1="10" x2="18" y2="10" stroke="var(--plum)" stroke-width="1.4"/></svg>
        www.amaralane.co.uk
      </li>
    </ul>
  </section>
</main>
</body>
</html>
```